Haldor Snekker AS
Buiness cards for haldor snekker as
Haldor Snekker AS - Construction
Creative Brief
Simple
Tobias Kranveldt
CEO
Lerkeskogveien 14 0587 OSLO Norway
post@haldorsnekker.example
www.haldorsnekker.example
Org. nr.: 836 402 517
Its for a company that expanse fast within big building sites
come up with something!?! we make your investment possible

```html
<!DOCTYPE html>
<html lang="en">
<head>
<meta charset="utf-8">
<title>Haldor Snekker AS – Business Cards</title>
<link rel="stylesheet" href="https://fonts.googleapis.com/css2?family=Open+Sans:wght@400;600;700&display=swap">
<style>
  :root {
    --stage: #454545;
    --brand-blue: #2c4b74;
    --card-white: #ffffff;
    --text-grey: #4a4a4a;
    --tagline: #c9d6e6;
  }
  html, body {
    margin: 0;
    padding: 0;
    width: 1200px;
    height: 751px;
    overflow: hidden;
    background: var(--stage);
    font-family: "Open Sans", Arial, sans-serif;
  }
  .canvas {
    position: relative;
    width: 1200px;
    height: 751px;
  }
  .card {
    position: absolute;
    width: 492px;
    height: 282px;
    box-sizing: border-box;
  }
  .card-front {
    left: 91px;
    top: 220px;
    background: var(--card-white);
  }
  .card-back {
    left: 619px;
    top: 218px;
    background: var(--brand-blue);
  }
  .front-band {
    position: absolute;
    left: 0;
    right: 0;
    top: 52px;
    height: 48px;
    background: var(--brand-blue);
  }
  .wordmark {
    position: absolute;
    display: flex;
    align-items: center;
    gap: 10px;
    color: var(--card-white);
    font-weight: 700;
    letter-spacing: 0.5px;
    white-space: nowrap;
  }
  .wordmark .mark-square {
    width: 16px;
    height: 16px;
    background: var(--card-white);
  }
  .card-front .wordmark {
    left: 50%;
    top: 52px;
    height: 48px;
    transform: translateX(-50%);
    font-size: 21px;
  }
  .card-back .wordmark {
    left: 50%;
    top: 126px;
    transform: translateX(-50%);
    font-size: 22px;
  }
  .person {
    position: absolute;
    left: 30px;
    top: 172px;
    color: var(--text-grey);
    font-size: 11.5px;
    line-height: 19px;
  }
  .person-name {
    color: var(--brand-blue);
    font-size: 16px;
    font-weight: 600;
    line-height: 22px;
  }
  .contacts {
    position: absolute;
    right: 22px;
    top: 174px;
    list-style: none;
    margin: 0;
    padding: 0;
    color: var(--text-grey);
    font-size: 11.5px;
    line-height: 19px;
    text-align: right;
  }
  .contacts li {
    display: flex;
    align-items: center;
    justify-content: flex-end;
    gap: 8px;
  }
  .contacts svg {
    width: 12px;
    height: 12px;
    fill: var(--brand-blue);
    flex: none;
  }
  .tagline {
    position: absolute;
    left: 56px;
    top: 236px;
    margin: 0;
    color: var(--tagline);
    font-size: 12px;
  }
</style>
</head>
<body>
<main class="canvas">
  <section class="card card-front" aria-label="Business card front">
    <div class="front-band"></div>
    <div class="wordmark"><span class="mark-square"></span>HALDOR SNEKKER AS</div>
    <div class="person">
      <div class="person-name">Tobias Kranveldt</div>
      <div class="person-role">CEO</div>
      <div class="person-address">Lerkeskogveien 14 0587 OSLO, Norway</div>
      <div class="person-org">Lin.: 836 402 517</div>
    </div>
    <ul class="contacts">
      <li>+47 9180 4427
        <svg viewBox="0 0 12 12" aria-hidden="true"><path d="M3.5 0h5a1 1 0 0 1 1 1v10a1 1 0 0 1-1 1h-5a1 1 0 0 1-1-1V1a1 1 0 0 1 1-1zm0 1.5v8h5v-8z"/></svg>
      </li>
      <li>+47 2250 6613
        <svg viewBox="0 0 12 12" aria-hidden="true"><path d="M1 4c0-2 2-3 5-3s5 1 5 3v1H8.5V3.8h-5V5H1zM2.5 6h7l1 5h-9z"/></svg>
      </li>
      <li>post@haldorsnekker.example
        <svg viewBox="0 0 12 12" aria-hidden="true"><path d="M0 2h12v1.2L6 7 0 3.2zM0 4.6l6 3.8 6-3.8V10H0z"/></svg>
      </li>
      <li>www.haldorsnekker.example
        <svg viewBox="0 0 12 12" aria-hidden="true"><path d="M6 0a6 6 0 1 0 0 12A6 6 0 0 0 6 0zm0 1.4a4.6 4.6 0 0 1 0 9.2 4.6 4.6 0 0 1 0-9.2zM5.3 3v6h1.4V3zM3 5.3v1.4h6V5.3z"/></svg>
      </li>
    </ul>
  </section>

  <section class="card card-back" aria-label="Business card back">
    <div class="wordmark"><span class="mark-square"></span>HALDOR SNEKKER AS</div>
    <p class="tagline">we make your investment possible</p>
  </section>
</main>
</body>
</html>
```